Bluepeak Resale Partners
Simplifying Inventory Management
Bluepeak Resale Partners - Automotive
Creative Brief
Bright & Fun-filled
Milo Tarkett
Owner
2715K N. Alder Ln Suite 348 Smyrna Ga 30082
Milo@BRPMotor.example
www.BRPMotor.example
Idea of dim outline of logo in background behind text maybe? Open to many ideas.
Initial thinking is logo on one side with tag, info side Im open from current modern,, cutting edge,professional, SImple...etc. Looking for clear and easy to read, yet catchy.

```html
<!DOCTYPE html>
<html lang="en">
<head>
<meta charset="utf-8">
<title>Bluepeak Resale Partners – Business Cards</title>
<link rel="stylesheet" href="https://fonts.googleapis.com/css2?family=Open+Sans:wght@400;600;700;800&display=swap">
<style>
  :root {
    --bg: #ece7df;
    --card: #ffffff;
    --brand-blue: #1d3f8f;
    --brand-red: #d62a2a;
    --ink: #2a3c6a;
    --ink-soft: #4b5567;
    --rule: #c7ccd6;
  }
  * { box-sizing: border-box; margin: 0; padding: 0; }
  html, body {
    width: 1200px; height: 852px; overflow: hidden;
    background: var(--bg);
    font-family: "Open Sans", Arial, sans-serif;
  }
  .stage { position: relative; width: 1200px; height: 852px; }

  .card {
    position: absolute;
    width: 540px; height: 310px;
    background: var(--card);
    border-radius: 22px;
    overflow: hidden;
    box-shadow: 0 6px 18px rgba(0,0,0,.18);
  }
  .card--front { left: 50px; top: 110px; }
  .card--back  { left: 610px; top: 430px; }

  .base-band {
    position: absolute; left: 0; bottom: 0;
    width: 100%; height: 46px;
    background: var(--brand-blue);
    border-top: 5px solid var(--brand-red);
  }

  .brand-name {
    font-weight: 800;
    color: var(--brand-blue);
    letter-spacing: .5px;
    display: flex; align-items: center; gap: 10px;
    line-height: 1.1;
  }
  .brand-dot {
    width: 16px; height: 16px; border-radius: 50%;
    background: var(--brand-blue); flex: none;
  }

  .person-name { font-weight: 700; color: var(--ink); font-size: 15px; }
  .person-role { font-weight: 600; color: var(--ink-soft); font-size: 11px; margin-top: 2px; }
  .address { font-size: 11px; color: var(--ink-soft); line-height: 1.5; }

  .divider { position: absolute; width: 1px; background: var(--rule); }

  .contact-list { list-style: none; font-size: 11px; color: var(--ink-soft); }
  .contact-list li { display: flex; align-items: center; gap: 7px; height: 17px; }
  .contact-list svg { width: 11px; height: 11px; flex: none; fill: var(--brand-blue); }

  .card--front .brand-name { position: absolute; left: 70px; top: 62px; font-size: 26px; }
  .card--front .identity { position: absolute; right: 300px; top: 148px; text-align: right; }
  .card--front .identity .address { margin-top: 12px; }
  .card--front .divider { left: 254px; top: 145px; height: 90px; }
  .card--front .contact-list { position: absolute; left: 268px; top: 146px; }

  .card--back .identity { position: absolute; left: 276px; top: 34px; }
  .card--back .identity .address { margin-top: 14px; }
  .card--back .brand-name { position: absolute; left: 28px; top: 148px; font-size: 18px; width: 220px; }
  .card--back .divider { left: 262px; top: 30px; height: 215px; }
  .card--back .contact-list { position: absolute; left: 276px; top: 160px; }
</style>
</head>
<body>
<main class="stage">

  <svg width="0" height="0" style="position:absolute">
    <defs>
      <symbol id="icon-phone" viewBox="0 0 24 24"><path d="M6.6 10.8a15 15 0 0 0 6.6 6.6l2.2-2.2a1 1 0 0 1 1-.25 11.4 11.4 0 0 0 3.6.57 1 1 0 0 1 1 1V20a1 1 0 0 1-1 1A17 17 0 0 1 3 4a1 1 0 0 1 1-1h3.5a1 1 0 0 1 1 1c0 1.25.2 2.45.57 3.57a1 1 0 0 1-.25 1z"/></symbol>
      <symbol id="icon-fax" viewBox="0 0 24 24"><path d="M6 2h12v6H6zM4 9h16a2 2 0 0 1 2 2v7h-4v4H6v-4H2v-7a2 2 0 0 1 2-2zm4 7v4h8v-4z"/></symbol>
      <symbol id="icon-mail" viewBox="0 0 24 24"><path d="M2 5h20v14H2zm2 2v.5l8 5 8-5V7l-8 5z"/></symbol>
      <symbol id="icon-web" viewBox="0 0 24 24"><path d="M12 2a10 10 0 1 0 0 20 10 10 0 0 0 0-20zm0 2c.9 0 2.2 2 2.7 5H9.3C9.8 6 11.1 4 12 4zM4.3 11h3a17 17 0 0 0 0 2h-3a8 8 0 0 1 0-2zm5 0h5.4a15 15 0 0 1 0 2H9.3a15 15 0 0 1 0-2zm7.4 0h3a8 8 0 0 1 0 2h-3a17 17 0 0 0 0-2zM9.3 15h5.4c-.5 3-1.8 5-2.7 5s-2.2-2-2.7-5z"/></symbol>
    </defs>
  </svg>

  <section class="card card--front">
    <div class="brand-name"><span class="brand-dot"></span>Bluepeak Resale Partners</div>

    <div class="identity">
      <p class="person-name">Milo Tarkett</p>
      <p class="person-role">Owner</p>
      <p class="address">2715K N. Alder Ln<br>Suite 348, Smyrna Ga 30082</p>
    </div>

    <div class="divider"></div>

    <ul class="contact-list">
      <li><svg><use href="#icon-phone"/></svg>770-555-0148</li>
      <li><svg><use href="#icon-fax"/></svg>888-555-0192</li>
      <li><svg><use href="#icon-mail"/></svg>Milo@BRPMotor.example</li>
      <li><svg><use href="#icon-web"/></svg>www.BRPMotor.example</li>
    </ul>

    <div class="base-band"></div>
  </section>

  <section class="card card--back">
    <div class="identity">
      <p class="person-name">Milo Tarkett</p>
      <p class="person-role">Owner</p>
      <p class="address">2715K N. Alder Ln<br>Suite 348, Smyrna Ga 30082</p>
    </div>

    <div class="divider"></div>

    <div class="brand-name"><span class="brand-dot"></span>Bluepeak Resale Partners</div>

    <ul class="contact-list">
      <li><svg><use href="#icon-phone"/></svg>770-555-0148</li>
      <li><svg><use href="#icon-fax"/></svg>888-555-0192</li>
      <li><svg><use href="#icon-mail"/></svg>Milo@BRPMotor.example</li>
      <li><svg><use href="#icon-web"/></svg>www.BRPMotor.example</li>
    </ul>

    <div class="base-band"></div>
  </section>

</main>
</body>
</html>
```